Veltrona5 website

Need to create a website for my business

Target Market(s)

Food ingredient companies, B2B

Industry/Entity Type

Food technology, food ingredients

Coding

Coded - Design and coding required

Number of Pages Required

2 page

Requirements
Nice to have
• Case studies, links to articles,

```html
<!DOCTYPE html>
<html lang="en">
<head>
<meta charset="utf-8">
<title>Veltrona5 — Food technology, food ingredients</title>
<link rel="stylesheet" href="https://fonts.googleapis.com/css2?family=Poppins:ital,wght@0,400;0,500;0,600;0,700;1,600&display=swap">
<style>
:root{
  --green:#0b7d12;
  --green-pale:#dcebd9;
  --ink:#2a2a2a;
  --text:#555;
  --muted:#8a8a8a;
  --dark:#3b3b3b;
  --btn:#333;
  --white:#fff;
  --line:#e4e4e4;
}
*{box-sizing:border-box;margin:0;padding:0}
html,body{width:1200px;height:4584px;overflow:hidden}
body{position:relative;background:var(--white);font-family:'Poppins',sans-serif;color:var(--ink)}
.abs{position:absolute}
a{color:inherit;text-decoration:none}

/* brand */
.brand{display:flex;align-items:center;gap:12px}
.brand-dot{width:28px;height:28px;border-radius:50%;background:var(--green)}
.brand-name{font-size:26px;font-weight:600;line-height:1}
.header-brand{left:89px;top:38px;color:var(--ink)}
.nav{left:427px;top:43px;display:flex;align-items:center;gap:20px;font-size:12px;letter-spacing:.2px}
.nav-home{width:16px;height:14px}
.search{left:895px;top:34px;width:216px;height:40px;border-radius:20px;background:#eee;display:flex;align-items:center;justify-content:space-between;padding:0 16px 0 20px;font-size:11px;color:var(--muted)}

/* hero */
.hero-title{left:89px;top:178px;font-size:48px;font-weight:600;line-height:53px;color:var(--ink);width:440px}
.hero-sub{left:89px;top:360px;font-size:17px;color:var(--ink)}
.btn{display:inline-flex;align-items:center;justify-content:center;background:var(--btn);color:var(--white);font-size:12px;font-weight:600;border-radius:22px;text-transform:uppercase}
.hero-btn{left:89px;top:409px;width:148px;height:43px}
.hero-photo{left:470px;top:110px;width:720px;height:560px;border-radius:50%;background:radial-gradient(ellipse at 45% 45%,#f4e7c9 0%,#f6efe1 35%,#fbf8f2 60%,rgba(255,255,255,0) 75%)}

/* stats */
.stats{left:0;top:820px;width:1200px;display:flex;justify-content:center}
.stat{width:241px;text-align:center;color:var(--white);position:relative}
.stat + .stat::before{content:"";position:absolute;left:0;top:10px;height:150px;border-left:1px solid rgba(255,255,255,.25)}
.stat svg{height:70px;width:80px;display:block;margin:14px auto 0}
.stat-num{font-size:38px;font-weight:600;line-height:1;margin-top:14px}
.stat-label{font-size:12px;font-weight:500;margin-top:12px;text-transform:uppercase}

/* features */
.feature-photo-a{left:0;top:1059px;width:623px;height:525px;background:radial-gradient(circle at 410px 303px,#6b4a35 0,#8a5c3c 150px,#b57a44 195px,rgba(181,122,68,0) 207px),radial-gradient(ellipse at 70px 300px,#7aa54c 0,#a9c986 60px,rgba(255,255,255,0) 120px)}
.feature-title{font-size:34px;font-weight:600;line-height:41px;color:var(--ink)}
.feature-text{font-size:14px;line-height:24px;color:var(--text)}
.f1-title{left:671px;top:1152px;width:440px}
.f1-text{left:671px;top:1306px;width:400px}
.f1-btn{left:671px;top:1477px;width:127px;height:45px}
.f2-title{left:89px;top:1734px;width:400px;font-size:33px;line-height:40px}
.rule{width:44px;border-top:2px solid var(--line)}
.f2-rule{left:89px;top:1872px}
.f2-text{left:89px;top:1891px;width:400px}
.f2-btn{left:89px;top:2060px;width:127px;height:42px}

/* section heading */
.section-title{left:0;width:1200px;text-align:center;font-size:34px;font-weight:600;color:var(--ink)}
.section-rule{left:577px;width:46px;border-top:2px solid var(--line)}

/* case studies */
.cases{left:0;top:2341px;width:1200px;height:397px;display:flex}
.case{flex:1;position:relative;color:var(--white)}
.case::after{content:"";position:absolute;inset:0;background:linear-gradient(180deg,rgba(0,0,0,0) 45%,rgba(0,0,0,.65) 100%)}
.case-info{position:absolute;left:32px;bottom:30px;z-index:1}
.case-price{font-size:17px;font-weight:600;opacity:.8}
.case-name{font-size:20px;font-weight:600;margin-top:2px}
.c1{background:linear-gradient(150deg,#4b5a33,#8c8c84 50%,#595955)}
.c2{background:linear-gradient(150deg,#6d5038,#5a7b3a 45%,#3a2e25)}
.c3{background:linear-gradient(150deg,#9a9a95,#cfbfb8 45%,#7e7b75)}
.c4{background:linear-gradient(150deg,#c99a2a,#2f3a2a 35%,#262626)}

/* testimonial */
.quote-photo{left:231px;top:2905px;width:346px;height:346px;border-radius:50%;background:radial-gradient(circle at 50% 45%,#d4551e 0,#c9643d 35%,#e7dcd4 70%);border:6px solid var(--white)}
.quote-text{left:632px;top:2958px;width:480px;font-size:30px;line-height:45px;font-style:italic;font-weight:600;color:var(--ink)}
.quote-author{left:629px;top:3156px;font-size:12px;font-weight:600;color:var(--green)}
.arrow{width:52px;height:52px;border-radius:50%;background:#e6e6e6;display:flex;align-items:center;justify-content:center;font-size:16px;color:var(--ink)}
.prev{left:629px;top:3196px}
.next{left:688px;top:3196px}
.spices{left:1066px;top:3133px;width:160px;height:285px;border-radius:80px 0 0 80px;background:radial-gradient(circle at 60% 50%,#c9772d 0,#b65424 40%,#8d6a48 70%,rgba(255,255,255,0) 75%)}

/* blog */
.blog{left:166px;top:3430px;display:flex;gap:20px}
.post{width:276px;height:397px;background:var(--white);box-shadow:0 4px 22px rgba(0,0,0,.08);padding:9px}
.post-img{height:197px}
.p1{background:linear-gradient(135deg,#3c3a38,#b9452d 50%,#5e4f3a)}
.p2{background:linear-gradient(135deg,#6e6c69,#d9b98a 50%,#5a5753)}
.p3{background:linear-gradient(135deg,#7c7a76,#7aa23a 40%,#b5304a 70%,#6a6864)}
.post-body{padding:0 14px}
.post-date{font-size:10px;color:var(--muted);margin-top:20px}
.post-title{font-size:15px;font-weight:600;margin-top:8px}
.post-text{font-size:11px;line-height:16px;color:var(--text);margin-top:8px}
.post-link{display:block;text-align:center;font-size:11px;font-weight:600;color:var(--green);margin-top:23px;text-transform:uppercase}

/* cta */
.cta{left:171px;top:3946px;width:852px;height:153px;border-radius:77px;background:var(--green);display:flex;align-items:center;justify-content:space-between;padding:0 83px 0 88px;z-index:2}
.cta-title{font-size:38px;font-weight:600;line-height:45px;color:var(--white)}
.cta-btn{background:var(--white);color:var(--ink);font-size:11px;font-weight:600;border-radius:24px;width:210px;height:48px;display:flex;align-items:center;justify-content:center;text-transform:uppercase}

/* footer */
.footer-brand{left:89px;top:4318px;color:var(--white)}
.footer-brand .brand-name{font-size:28px}
.socials{left:131px;top:4368px;display:flex;gap:10px}
.socials span{width:41px;height:41px;border-radius:50%;background:#555}
.fcol{color:var(--white)}
.fcol h4{font-size:19px;font-weight:600;margin-bottom:22px}
.links li{list-style:none;font-size:12px;margin-bottom:14px}
.links li::before{content:"›";margin-right:8px}
.loc{left:443px;top:4228px}
.contact{left:619px;top:4228px}
.contact-item{display:flex;gap:10px;font-size:12px;line-height:19px;margin-bottom:22px}
.contact-item svg{flex:none;margin-top:3px}
.news{left:851px;top:4230px;width:260px}
.news p{font-size:12px;line-height:18px}
.news-form{display:flex;margin-top:18px;height:44px}
.news-input{flex:1;background:var(--white);border-radius:22px 0 0 22px;font-size:11px;color:var(--muted);display:flex;align-items:center;padding-left:18px}
.news-send{width:42px;background:var(--green);border-radius:0 22px 22px 0;display:flex;align-items:center;justify-content:center}
.copyright{left:0;top:4545px;width:1200px;text-align:center;font-size:12px;font-weight:600;color:var(--white)}
.chat{left:1131px;top:4500px;width:44px;height:44px;border-radius:50%;background:var(--green);display:flex;align-items:center;justify-content:center}
</style>
</head>
<body>

<svg class="abs" style="left:0;top:0" width="1200" height="1035" viewBox="0 0 1200 1035" aria-hidden="true">
  <path d="M0 600 C120 535 270 525 410 590 C560 660 700 770 860 778 L860 1035 H0Z" fill="#e5e5e5"/>
  <path d="M0 690 C150 640 300 650 450 705 C600 765 740 790 860 776 C1010 760 1110 650 1200 545 V1035 H0Z" fill="var(--green)"/>
</svg>
<div class="abs hero-photo" role="img" aria-label="Breakfast table from above with plates of fruit, pancakes, berries and a teapot"></div>

<header>
  <div class="abs brand header-brand">
    <span class="brand-dot"></span>
    <span class="brand-name">Veltrona5</span>
  </div>
  <nav class="abs nav">
    <svg class="nav-home" viewBox="0 0 16 14"><path d="M8 0 L16 7 H13 V14 H10 V9 H6 V14 H3 V7 H0Z" fill="var(--green)"/></svg>
    <a>MENU</a><a>RESERVATIONS</a><a>CASE STUDIES</a><a>ARTICLES</a><a>CONTACT</a>
  </nav>
  <div class="abs search"><span>Search here...</span>
    <svg width="12" height="12" viewBox="0 0 12 12"><circle cx="5" cy="5" r="3.8" fill="none" stroke="#333" stroke-width="1.5"/><path d="M8 8 L11 11" stroke="#333" stroke-width="1.5"/></svg>
  </div>
</header>

<section>
  <h1 class="abs hero-title">Good food choices are good investments.</h1>
  <p class="abs hero-sub">Food technology, Food ingredients</p>
  <a class="abs btn hero-btn">Book a table</a>
</section>

<section class="abs stats">
  <div class="stat">
    <svg viewBox="0 0 80 70"><rect x="8" y="18" width="26" height="48" rx="3" fill="#fff"/><rect x="18" y="4" width="4" height="16" fill="#fff"/><rect x="36" y="38" width="38" height="8" rx="4" fill="#fff"/><rect x="36" y="50" width="38" height="6" rx="3" fill="#fff"/><rect x="36" y="60" width="38" height="6" rx="3" fill="#fff"/></svg>
    <div class="stat-num">1287+</div><div class="stat-label">Food</div>
  </div>
  <div class="stat">
    <svg viewBox="0 0 80 70"><circle cx="26" cy="22" r="18" fill="none" stroke="#fff" stroke-width="5"/><path d="M26 12 V22 H34" stroke="#fff" stroke-width="4" fill="none"/><rect x="14" y="42" width="38" height="18" fill="#fff"/><path d="M52 44 H66 L74 54 V60 H52Z" fill="#fff"/><circle cx="26" cy="63" r="6" fill="#fff" stroke="var(--green)" stroke-width="2"/><circle cx="62" cy="63" r="6" fill="#fff" stroke="var(--green)" stroke-width="2"/></svg>
    <div class="stat-num">5786+</div><div class="stat-label">Delivery</div>
  </div>
  <div class="stat">
    <svg viewBox="0 0 80 70"><circle cx="18" cy="20" r="9" fill="#fff"/><circle cx="62" cy="20" r="9" fill="#fff"/><circle cx="40" cy="18" r="12" fill="#fff"/><path d="M4 58 C4 38 32 38 32 58Z" fill="#fff"/><path d="M48 58 C48 38 76 38 76 58Z" fill="#fff"/><path d="M20 66 C20 34 60 34 60 66Z" fill="#fff"/></svg>
    <div class="stat-num">1440+</div><div class="stat-label">Customer</div>
  </div>
  <div class="stat">
    <svg viewBox="0 0 80 70"><polygon points="40,2 44,12 55,12 46,18 49,28 40,22 31,28 34,18 25,12 36,12" fill="#fff"/><polygon points="16,16 19,23 27,23 21,28 23,35 16,31 9,35 11,28 5,23 13,23" fill="#fff"/><polygon points="64,16 67,23 75,23 69,28 71,35 64,31 57,35 59,28 53,23 61,23" fill="#fff"/><path d="M26 68 V44 H32 L40 32 C44 32 44 36 43 42 H54 C57 42 57 46 56 48 L52 66 H32Z" fill="#fff"/></svg>
    <div class="stat-num">7110+</div><div class="stat-label">Rating</div>
  </div>
</section>

<section>
  <div class="abs feature-photo-a" role="img" aria-label="Bowl of beef noodle soup with chili, lime and chopsticks beside a tossed salad"></div>
  <h2 class="abs feature-title f1-title">We pride ourselves on making real food from the best ingredients.</h2>
  <p class="abs feature-text f1-text">Lorem ipsum dolor sit amet, consectetur adipiscing elit. Etiam et purus a odio finibus bibendum in sit amet leo. Mauris feugiat erat tellus. Far far away, behind the word mountains, far from the countries Vokalia and Consonantia, there live the blind texts consectetur adipiscing...</p>
  <a class="abs btn f1-btn">Read more</a>
</section>

<section>
  <svg class="abs" style="left:600px;top:1608px" width="600" height="550" viewBox="0 0 600 550" aria-hidden="true">
    <path d="M10 190 C10 70 100 0 200 8 C300 15 380 60 600 120 V540 L20 420Z" fill="var(--green-pale)"/>
  </svg>
  <svg class="abs" style="left:600px;top:1608px" width="600" height="550" viewBox="0 0 600 550" role="img" aria-label="Plates of grilled steak with lettuce, red onion, chili and cashews beside a small bowl of sauce">
    <defs><linearGradient id="plateShade" x1="0" y1="0" x2="1" y2="1"><stop offset="0" stop-color="#7b7c72"/><stop offset=".5" stop-color="#5a4a3d"/><stop offset="1" stop-color="#3e3f3a"/></linearGradient></defs>
    <path d="M42 120 C70 40 150 30 230 45 C330 60 450 100 600 160 V430 C480 500 300 560 180 520 C80 490 40 420 42 300Z" fill="url(#plateShade)"/>
  </svg>
  <h2 class="abs feature-title f2-title">We make everything by hand with the best possible ingredients.</h2>
  <div class="abs rule f2-rule"></div>
  <p class="abs feature-text f2-text">Lorem ipsum dolor sit amet, consectetur adipiscing elit. Etiam et purus a odio finibus bibendum in sit amet leo. Mauris feugiat erat tellus. Far far away, behind the word mountains, far from the countries Vokalia and Consonantia, there live the blind texts consectetur adipiscing...</p>
  <a class="abs btn f2-btn">Read more</a>
</section>

<section>
  <h2 class="abs section-title" style="top:2250px">Veltrona5 case studies</h2>
  <div class="abs section-rule" style="top:2309px"></div>
  <div class="abs cases">
    <article class="case c1" role="img" aria-label="Avocado toast topped with a poached egg and chili flakes"><div class="case-info"><div class="case-price">$25.00</div><div class="case-name">Some heading here</div></div></article>
    <article class="case c2" role="img" aria-label="Bowl of fresh green salad with tomato and red onion on a wooden table"><div class="case-info"><div class="case-price">$25.00</div><div class="case-name">Some heading here</div></div></article>
    <article class="case c3" role="img" aria-label="Raw chicken pieces with cherry tomatoes and spices on a grey surface"><div class="case-info"><div class="case-price">$25.00</div><div class="case-name">Some heading here</div></div></article>
    <article class="case c4" role="img" aria-label="Dark plate of mixed salad beside a glass of orange juice and a fork"><div class="case-info"><div class="case-price">$25.00</div><div class="case-name">Some heading here</div></div></article>
  </div>
</section>

<section>
  <svg class="abs" style="left:90px;top:2840px" width="220" height="475" viewBox="0 0 220 475" aria-hidden="true">
    <path d="M140 2 C40 80 0 170 3 250 C6 340 60 420 140 472 L215 410 C160 370 130 310 130 240 C130 170 160 110 215 70Z" fill="var(--green)"/>
  </svg>
  <div class="abs quote-photo" role="img" aria-label="Smiling woman in an orange sweater eating a slice of pizza"></div>
  <svg class="abs" style="left:775px;top:2862px" width="190" height="95" viewBox="0 0 190 95" aria-hidden="true">
    <path d="M5 95 V55 C5 20 30 2 70 0 V25 C50 27 42 38 42 55 H80 V95Z M105 95 V55 C105 20 130 2 170 0 V25 C150 27 142 38 142 55 H180 V95Z" fill="#eef2ec"/>
  </svg>
  <blockquote class="abs quote-text">“The quality of the products comes from the quality of the environment in which they are created”</blockquote>
  <p class="abs quote-author">Marta Quintal – Veltrona5</p>
  <span class="abs arrow prev">‹</span>
  <span class="abs arrow next">›</span>
  <div class="abs spices" role="img" aria-label="Wooden spoons filled with assorted ground spices"></div>
</section>

<section>
  <h2 class="abs section-title" style="top:3340px">Blog articles</h2>
  <div class="abs section-rule" style="top:3399px"></div>
  <div class="abs blog">
    <article class="post"><div class="post-img p1" role="img" aria-label="Table with bowls of curry, fries and dipping sauces"></div><div class="post-body"><p class="post-date">25-05-2022</p><h3 class="post-title">Some blog heading goes...</h3><p class="post-text">Aenean sollicitudin lorem quis bibendum auctor nisi elit consequat ipsum, nec sagittis sem...</p><a class="post-link">View detail</a></div></article>
    <article class="post"><div class="post-img p2" role="img" aria-label="Fork twirling spaghetti over a plate of pasta"></div><div class="post-body"><p class="post-date">25-05-2022</p><h3 class="post-title">Some blog heading goes...</h3><p class="post-text">Aenean sollicitudin lorem quis bibendum auctor nisi elit consequat ipsum, nec sagittis sem...</p><a class="post-link">View detail</a></div></article>
    <article class="post"><div class="post-img p3" role="img" aria-label="Colourful bowl of salad with avocado and red cabbage"></div><div class="post-body"><p class="post-date">25-05-2022</p><h3 class="post-title">Some blog heading goes...</h3><p class="post-text">Aenean sollicitudin lorem quis bibendum auctor nisi elit consequat ipsum, nec sagittis sem...</p><a class="post-link">View detail</a></div></article>
  </div>
</section>

<svg class="abs" style="left:0;top:3990px" width="1200" height="594" viewBox="0 0 1200 594" aria-hidden="true">
  <path d="M0 150 C250 120 500 150 760 110 C960 80 1100 40 1200 50 V594 H0Z" fill="var(--dark)"/>
  <path d="M0 150 C120 250 300 270 460 200 C330 200 170 190 0 150Z" fill="var(--white)"/>
</svg>

<section class="abs cta">
  <h2 class="cta-title">Baked fresh daily by<br>bakers with passion.</h2>
  <a class="cta-btn">Get in touch with us</a>
</section>

<footer>
  <div class="abs brand footer-brand">
    <span class="brand-dot"></span>
    <span class="brand-name">Veltrona5</span>
  </div>
  <div class="abs socials" aria-label="Social links"><span></span><span></span><span></span><span></span></div>

  <div class="abs fcol loc">
    <h4>Locations</h4>
    <ul class="links"><li>Home</li><li>Menu</li><li>Reservations</li><li>Case studies</li><li>Articles</li><li>Contact Us</li></ul>
  </div>

  <div class="abs fcol contact">
    <h4>Contact info</h4>
    <div class="contact-item"><svg width="13" height="10" viewBox="0 0 13 10"><rect width="13" height="10" rx="1" fill="#fff"/><path d="M0 1 L6.5 6 L13 1" stroke="var(--dark)" fill="none"/></svg><span>Email:<br>info@example.com</span></div>
    <div class="contact-item"><svg width="13" height="13" viewBox="0 0 13 13"><path d="M3 0 L5 3 L3.5 5 C4.5 7 6 8.5 8 9.5 L10 8 L13 10 L11.5 13 C5 12 1 8 0 1.5Z" fill="#fff"/></svg><span>Phone:<br>+08 123 456 7890</span></div>
    <div class="contact-item"><svg width="11" height="15" viewBox="0 0 11 15"><path d="M5.5 0 C8.5 0 11 2.3 11 5.3 C11 9 5.5 15 5.5 15 C5.5 15 0 9 0 5.3 C0 2.3 2.5 0 5.5 0Z" fill="#fff"/><circle cx="5.5" cy="5.3" r="2" fill="var(--dark)"/></svg><span>Location:<br>Some address line goes<br>here city name country</span></div>
  </div>

  <div class="abs fcol news">
    <h4>Newsletter</h4>
    <p>Subscribe to our email address to get the latest news.</p>
    <div class="news-form"><div class="news-input">✉&nbsp; Enter Your Email...</div>
      <div class="news-send"><svg width="16" height="16" viewBox="0 0 16 16"><path d="M0 7 L16 0 L11 16 L8 9Z" fill="#fff"/></svg></div>
    </div>
  </div>

  <p class="abs copyright">© Copyright 2022 | All Rights Reserved</p>
  <div class="abs chat"><svg width="22" height="18" viewBox="0 0 22 18"><path d="M11 0 C17 0 22 3.5 22 8 C22 12.5 17 16 11 16 L4 18 L6 14 C2 12.5 0 10.5 0 8 C0 3.5 5 0 11 0Z" fill="#fff"/><circle cx="6.5" cy="8" r="1.5" fill="var(--green)"/><circle cx="11" cy="8" r="1.5" fill="var(--green)"/><circle cx="15.5" cy="8" r="1.5" fill="var(--green)"/></svg></div>
</footer>

</body>
</html>
```